New Attorney in Non-Traditional Field Needs Creative Edgy Legal Business Card with Side Business Not

I need a new personal business card. Away from the silver lettering on heavy white card stock, Velvet Harbor anyone? I'm newly admitted to the CA bar, I started my own small side-business in sales, I'm arbitrating on a part time basis, and I'm creating a ClipTower channel about current news from young professionals' perspective in January. On the side I've been taking a lot of home buying negotiation classes, and I do a lot of yoga. It would be my dream job to advise clients in the startup/entrepreneurial world. I would like my Cliptower channel, website (www.marenquill.example/dankorbel), phone number, email, admittance #, and link for worklinx featured on my card. The colors and message of homepage www.bluefernmat.example really speak to me. Often I'll read that Hedda Pallin quote about doing one thing for your brand everyday, and I believe it in wholeheartedly.
Updates

Merrin's design has been accepted with very minimal changes. Thank you all for your submissions. This has been a fun experience.

Target Market(s)

all young attorneys, small startups, small tech, potential employers, networking events for lawyers and other young professionals

Industry/Entity Type

Business

Contact Information for Business Card

Dorothea K. Banfield, Esq.
Attorney bar card number
Ph (555) 407-1186
Email Dot.Banfield@postkite.example
Work linx website
Cliptower Channel coming soon!
Maren & Quill website

Font styles to use
Sans Serif
Decorative

Requirements
Must have
• A simple image or logo that can transition to other products as I build my brand. Great colors. Maybe all white & gold? Maybe a cool blues/purples motif?

```html
<!DOCTYPE html>
<html lang="en">
<head>
<meta charset="utf-8">
<title>Dorothea K. Banfield, Esq. — Business Card</title>
<link rel="stylesheet" href="https://fonts.googleapis.com/css2?family=Great+Vibes&family=Cinzel:wght@400&family=Varela+Round&display=swap">
<style>
  :root {
    --gold: #c99a2e;
    --gold-light: #f2d37a;
    --gold-deep: #a8791c;
    --card: #f7f9fa;
    --card-shade: #e3e9ed;
    --backdrop: #e9e6e1;
  }
  * { box-sizing: border-box; margin: 0; padding: 0; }
  html, body { width: 1200px; height: 797px; overflow: hidden; }
  body {
    background: var(--backdrop);
    position: relative;
    font-family: "Varela Round", sans-serif;
  }
  .card {
    position: absolute;
    left: 290px;
    width: 620px;
    height: 354px;
    background: var(--card);
    box-shadow: 0 4px 14px rgba(0,0,0,0.18);
    overflow: hidden;
  }
  .card--front { top: 30px; }
  .card--back { top: 413px; }

  .card-texture {
    position: absolute;
    inset: 0;
    background:
      linear-gradient(120deg, rgba(255,255,255,0.9) 0%, rgba(255,255,255,0) 40%),
      linear-gradient(200deg, rgba(227,233,237,0.8) 0%, rgba(247,249,250,0) 55%),
      linear-gradient(135deg, #ffffff 0%, var(--card) 50%, var(--card-shade) 100%);
  }

  .gold-rule {
    position: absolute;
    height: 4px;
    background: linear-gradient(90deg, var(--gold-deep), var(--gold-light), var(--gold));
  }
  .rule-top { left: 410px; right: 0; top: 36px; }
  .rule-name { left: 0; width: 190px; top: 96px; }
  .rule-mid { left: 0; right: 0; top: 156px; }
  .rule-low { left: 0; width: 300px; top: 192px; height: 3px; }

  .name-script {
    position: absolute;
    left: 170px; top: 8px;
    font-family: "Great Vibes", cursive;
    font-size: 44px;
    color: var(--gold);
    line-height: 1;
  }
  .name-caps {
    position: absolute;
    left: 196px; top: 58px;
    font-family: "Cinzel", serif;
    font-size: 32px;
    letter-spacing: 2px;
    color: var(--gold);
    line-height: 1;
  }
  .name-caps .suffix { font-size: 17px; letter-spacing: 0; }

  .contact {
    position: absolute;
    left: 0; width: 560px;
    text-align: center;
    color: var(--gold);
    line-height: 1;
  }
  .contact-admit { top: 108px; font-size: 15px; letter-spacing: 1px; }
  .contact-email { top: 128px; font-size: 21px; }
  .contact-site { top: 168px; font-size: 17px; }
  .contact-clip { top: 214px; font-size: 17px; }
  .contact-work { top: 246px; font-size: 17px; }
  .contact-phone { top: 282px; font-size: 21px; letter-spacing: 1px; }

  .brand-mark {
    position: absolute;
    display: flex;
    align-items: center;
    color: var(--gold);
    font-family: "Varela Round", sans-serif;
    line-height: 1;
  }
  .brand-dot {
    border: 2px solid var(--gold);
    border-radius: 50%;
    flex: none;
  }
  .brand-mark--small { left: 470px; top: 226px; gap: 8px; font-size: 18px; }
  .brand-mark--small .brand-dot { width: 20px; height: 20px; }
  .brand-mark--large {
    left: 0; right: 0; top: 0; bottom: 0;
    justify-content: center;
    gap: 24px;
    font-size: 72px;
  }
  .brand-mark--large .brand-dot { width: 64px; height: 64px; border-width: 5px; }
</style>
</head>
<body>
  <section class="card card--front" aria-label="Card front with contact details">
    <div class="card-texture" role="img" aria-label="Faint white faceted texture"></div>
    <div class="gold-rule rule-top"></div>
    <div class="gold-rule rule-name"></div>
    <div class="gold-rule rule-mid"></div>
    <div class="gold-rule rule-low"></div>

    <div class="name-script">Dorothea K.</div>
    <div class="name-caps">BANFIELD<span class="suffix">, Esq</span></div>

    <div class="contact contact-admit">admittance #</div>
    <div class="contact contact-email">Dot.Banfield@postkite.example</div>
    <div class="contact contact-site">www.marenquill.example/sites/dankorbel</div>
    <div class="contact contact-clip">www.cliptower.example/</div>
    <div class="contact contact-work">www.worklinx.example/</div>
    <div class="contact contact-phone">(555) 407-1186</div>

    <div class="brand-mark brand-mark--small"><span class="brand-dot"></span><span>Banfield</span></div>
  </section>

  <section class="card card--back" aria-label="Card back with brand name">
    <div class="card-texture" role="img" aria-label="Faint white faceted texture"></div>
    <div class="brand-mark brand-mark--large"><span class="brand-dot"></span><span>Banfield</span></div>
  </section>
</body>
</html>
```